Redesign of Business Card to look more professional and stand out

Business card design. You can lean more about our company by going to dkrfabworks.example. Raised letters would be nice. Company name & Address
DK&R
418 Wendlow Ridge Drive, Suite 340
Ridgeford, AL 35990

You can use my name and title: Glenn Harwick
Business Development Manager

Target Market(s)

Heavy Industrial market, i.e. utilities, chemical plants, paper mills, construction companies

Industry/Entity Type

Construction

Contact Information for Business Card

We provide Project Management & Project Support Services

Font styles to use
Serif

Requirements
Must have
• Company name & Address
• DK&R
• 418 Wendlow Ridge Drive, Suite 340
• Ridgeford, AL 35990
Nice to have
• ideas for the back of the card
Should not have
• no crazy colors. needs to look professional and standout.

```html
<!DOCTYPE html>
<html lang="en">
<head>
<meta charset="utf-8">
<title>DK&amp;R Business Card</title>
<link href="https://fonts.googleapis.com/css2?family=Quicksand:wght@400;500;700&display=swap" rel="stylesheet">
<style>
  :root {
    --backdrop: #9a9a9a;
    --card-navy: #1e3564;
    --emboss-navy: #233c6d;
    --accent-blue: #4a68a8;
    --label-blue: #5a78b8;
    --ink-white: #ffffff;
  }
  * { margin: 0; padding: 0; box-sizing: border-box; }
  html, body {
    width: 1200px;
    height: 897px;
    overflow: hidden;
    background: var(--backdrop);
    font-family: "Quicksand", sans-serif;
  }
  .canvas {
    width: 1200px;
    height: 897px;
    display: flex;
    flex-direction: column;
    align-items: center;
    justify-content: center;
    gap: 50px;
  }
  .card {
    position: relative;
    width: 600px;
    height: 343px;
    background: var(--card-navy);
    color: var(--ink-white);
    overflow: hidden;
  }
  .card-front .wordmark {
    position: absolute;
    left: 34px;
    top: 34px;
    font-size: 66px;
    font-weight: 700;
    letter-spacing: 1px;
    line-height: 1;
    color: var(--ink-white);
  }
  .card-front .divider {
    position: absolute;
    left: 238px;
    top: 120px;
    width: 2px;
    height: 196px;
    background: var(--accent-blue);
  }
  .card-front .identity {
    position: absolute;
    left: 262px;
    top: 132px;
  }
  .identity .person-name {
    font-size: 34px;
    font-weight: 500;
    line-height: 1.05;
    letter-spacing: 0.5px;
  }
  .identity .person-title {
    font-size: 11px;
    font-weight: 500;
    letter-spacing: 1.4px;
    text-transform: uppercase;
    color: var(--label-blue);
    margin-top: 2px;
  }
  .contact-list {
    position: absolute;
    left: 262px;
    top: 212px;
    display: grid;
    grid-template-columns: 62px auto;
    row-gap: 6px;
    align-items: baseline;
  }
  .contact-list dt {
    font-size: 9px;
    font-weight: 500;
    letter-spacing: 1px;
    text-transform: uppercase;
    color: var(--label-blue);
  }
  .contact-list dd {
    font-size: 13.5px;
    font-weight: 500;
    line-height: 1.3;
    color: var(--ink-white);
  }
  .card-back {
    display: flex;
    align-items: center;
    justify-content: center;
  }
  .card-back .raised-name {
    font-size: 150px;
    font-weight: 700;
    letter-spacing: 4px;
    color: var(--emboss-navy);
    line-height: 1;
  }
</style>
</head>
<body>
  <main class="canvas">
    <section class="card card-front" aria-label="Business card front">
      <div class="wordmark">DK&amp;R</div>
      <div class="divider"></div>
      <div class="identity">
        <p class="person-name">Glenn Harwick</p>
        <p class="person-title">Business Development Manager</p>
      </div>
      <dl class="contact-list">
        <dt>Phone</dt><dd>555.010.0148</dd>
        <dt>Email</dt><dd>harwickg@dkr-projectmgt.example</dd>
        <dt>Web</dt><dd>www.dkrfabworks.example</dd>
        <dt>Address</dt><dd>418 Wendlow Ridge Drive, Suite 340<br>Ridgeford, AL 35990</dd>
      </dl>
    </section>
    <section class="card card-back" aria-label="Business card back">
      <div class="raised-name">DK&amp;R</div>
    </section>
  </main>
</body>
</html>
```